Vorra Fleet business card

I am needing a business card that at a glance shows all the services that we provide emphasizing some more than others. We are a Fleet and Compliance management company as well as a software company. We provide outsourced solutions for PXM compliance and HR services via our own software.
In addition, we do
drug testing
GPS
Cameras
Electronic DVIRS
ELD's

Target Market(s)

Transportation company owners

Industry/Entity Type

Transportation supplier

Contact Information for Business Card

the card should inform potential customers what we do

Other font styles liked:
• I have added brand guidelines. See attached

Requirements
Must have
• See description
Should not have
• Colors outside my brand guide. See attached

```html
<!DOCTYPE html>
<html lang="en">
<head>
<meta charset="utf-8">
<title>Vorra Fleet business card</title>
<link rel="stylesheet" href="https://fonts.googleapis.com/css2?family=Open+Sans:wght@400;700&display=swap">
<style>
  :root {
    --navy: #15162b;
    --red: #e8323a;
    --white: #ffffff;
    --ink: #1d1d22;
    --shade: #a5a5aa;
    --backdrop: #e6e6e8;
  }
  * { margin: 0; padding: 0; box-sizing: border-box; }
  html, body { width: 1200px; height: 1115px; overflow: hidden; }
  body {
    background: var(--backdrop);
    font-family: "Open Sans", Arial, sans-serif;
    position: relative;
  }
  .card {
    position: absolute;
    left: 250px;
    width: 700px;
    height: 400px;
    border-radius: 20px;
    overflow: hidden;
  }
  .card--front { top: 131px; background: var(--white); }
  .card--back { top: 585px; background: var(--navy); }

  .front-wave { position: absolute; inset: 0; width: 700px; height: 400px; }

  .contact-block {
    position: absolute;
    right: 25px;
    top: 38px;
    text-align: right;
    color: var(--white);
  }
  .contact-name { color: var(--red); font-size: 27px; font-weight: 400; line-height: 1.2; letter-spacing: 0.2px; }
  .contact-role { font-size: 19px; line-height: 1.3; margin-bottom: 22px; }
  .contact-list { list-style: none; font-size: 16px; line-height: 21px; }
  .contact-list li { display: flex; justify-content: flex-end; align-items: center; gap: 6px; }
  .contact-list svg { width: 12px; height: 12px; fill: var(--red); flex: none; }
  .address { font-style: normal; font-size: 16px; line-height: 21.5px; margin-top: 22px; }

  .brand {
    position: absolute;
    display: flex;
    align-items: center;
    gap: 10px;
    font-weight: 700;
  }
  .brand-mark { width: 14px; height: 14px; background: var(--red); flex: none; }
  .brand--front { left: 25px; top: 245px; font-size: 42px; color: var(--navy); }
  .brand--back { left: 0; right: 0; top: 62px; justify-content: center; font-size: 48px; color: var(--white); }

  .tagline {
    position: absolute;
    left: 24px;
    top: 336px;
    font-size: 14px;
    line-height: 19.5px;
    color: var(--ink);
    letter-spacing: 0.2px;
  }

  .service-list {
    position: absolute;
    top: 220px;
    list-style: none;
    color: var(--white);
    font-size: 17px;
    line-height: 24px;
    letter-spacing: 0.2px;
  }
  .service-list li { display: flex; align-items: center; gap: 8px; }
  .service-list li::before,
  .service-list--right li::after {
    content: "";
    width: 6px; height: 6px; border-radius: 50%;
    background: var(--red); flex: none;
  }
  .service-list--left { left: 25px; }
  .service-list--right { right: 25px; text-align: right; }
  .service-list--right li { justify-content: flex-end; }
  .service-list--right li::before { display: none; }
</style>
</head>
<body>

<section class="card card--front" aria-label="Card front">
  <svg class="front-wave" viewBox="0 0 700 400" aria-hidden="true">
    <path d="M8,8 C150,34 232,122 312,200 C392,282 522,362 700,404 L700,0 L8,0 Z" fill="var(--shade)"/>
    <path d="M8,6 C150,28 234,116 314,194 C396,274 524,356 700,398 L700,0 L8,0 Z" fill="var(--navy)"/>
    <path d="M6,6 C120,30 200,70 300,190 C220,100 140,40 6,12 Z" fill="var(--red)"/>
  </svg>

  <div class="contact-block">
    <h1 class="contact-name">DANA KOWALCZYK</h1>
    <p class="contact-role">Co-Founder</p>
    <ul class="contact-list">
      <li>555.014.2231 <svg viewBox="0 0 12 12"><path d="M1,4 Q6,0 11,4 L10,6 L8,5 L8,4 Q6,3 4,4 L4,5 L2,6 Z M3,6 L9,6 L10,11 L2,11 Z"/></svg></li>
      <li>555.019.6470 <svg viewBox="0 0 12 12"><path d="M1,4 Q6,0 11,4 L10,6 L8,5 L8,4 Q6,3 4,4 L4,5 L2,6 Z M3,6 L9,6 L10,11 L2,11 Z"/></svg></li>
      <li>info@vorrafleet.com <svg viewBox="0 0 12 12"><path d="M0,2 L12,2 L12,10 L0,10 Z" /><path d="M0,2 L6,7 L12,2" fill="none" stroke="var(--navy)" stroke-width="1"/></svg></li>
      <li>www.vorrafleet.com <svg viewBox="0 0 12 12"><circle cx="6" cy="6" r="5" fill="none" stroke="var(--red)" stroke-width="1.2"/><ellipse cx="6" cy="6" rx="2" ry="5" fill="none" stroke="var(--red)" stroke-width="1"/><path d="M1,6 L11,6" stroke="var(--red)" stroke-width="1"/></svg></li>
    </ul>
    <address class="address">
      Company Street, 1265984<br>
      Suite/Bldg, Park Ave<br>
      City, Zip Code
    </address>
  </div>

  <div class="brand brand--front">
    <span class="brand-name">Vorra Fleet</span>
    <span class="brand-mark"></span>
  </div>

  <p class="tagline">
    Vorra Fleet, Safety &amp; Compliance,Hr and Compliane Services<br>
    Software and Fleet Services
  </p>
</section>

<section class="card card--back" aria-label="Card back">
  <div class="brand brand--back">
    <span class="brand-name">Vorra Fleet</span>
    <span class="brand-mark"></span>
  </div>

  <ul class="service-list service-list--left">
    <li>Drug Testing</li>
    <li>GPS Services</li>
    <li>Cameras Services</li>
    <li>Electronic DVIRS Services</li>
    <li>ELD's Services</li>
    <li>Safty Rating Upgrade</li>
  </ul>

  <ul class="service-list service-list--right">
    <li>Fleet Management</li>
    <li>Software and Fleet Services</li>
    <li>Limo Logs Services</li>
    <li>Pocket Fleet Mangers</li>
    <li>Mock and PXM Audit</li>
    <li>Complaince &amp; Hr Services</li>
  </ul>
</section>

</body>
</html>
```